Business cards Marta Keller Sport & Events

I need new business cards to match my new logo design for my company called "Marta Keller Sport & Events". I'm based in Germany.
With my company, I offer different services in the context of sport.

Marta Keller owner

Marta Keller Sports & Events
Birkendorfer Weg 14
D-63158 Offenbach

+49 69 / 31 52 94 07
info@marta-keller-sport.example
www.marta-keller-sport.example

Contact Information for Business Card

Marta Keller Inhaberin Marta Keller Sport & Events Birkendorfer Weg 14 D-63158 Offenbach +49 69 / 31 52 94 07 info@marta-keller-sport.example www.marta-keller-sport.example

Requirements
Must have
• Logo | Double sided business card

```html
<!DOCTYPE html>
<html lang="de">
<head>
<meta charset="utf-8">
<title>Marta Keller Sport &amp; Events – Visitenkarte</title>
<link rel="stylesheet" href="https://fonts.googleapis.com/css2?family=Arimo:wght@400;700&family=Michroma&display=swap">
<style>
  :root {
    --stage: #2a2a2a;
    --card: #0b0b0b;
    --accent: #f5a01a;
    --text: #e6e6e6;
    --divider: #3a3a3a;
  }
  * { margin: 0; padding: 0; box-sizing: border-box; }
  html, body { width: 1200px; height: 900px; overflow: hidden; }
  body {
    background: var(--stage);
    font-family: "Arimo", Arial, sans-serif;
    position: relative;
  }
  .card {
    position: absolute;
    left: 280px;
    width: 640px;
    height: 400px;
    background: var(--card);
    box-shadow: 0 12px 30px rgba(0,0,0,.55);
  }
  .card--contact { top: 40px; }
  .card--brand { top: 460px; }

  .brand-lockup {
    position: absolute;
    display: flex;
    flex-direction: column;
    align-items: center;
    gap: 18px;
  }
  .brand-lockup__dot {
    border-radius: 50%;
    background: var(--accent);
  }
  .brand-lockup__name {
    color: #ffffff;
    font-family: "Arimo", Arial, sans-serif;
    font-weight: 700;
    text-transform: uppercase;
    letter-spacing: .12em;
    text-align: center;
    line-height: 1.25;
  }

  .card--contact .brand-lockup { left: 30px; top: 110px; width: 250px; }
  .card--contact .brand-lockup__dot { width: 96px; height: 96px; }
  .card--contact .brand-lockup__name { font-size: 18px; }

  .card--brand .brand-lockup { left: 0; right: 0; top: 95px; }
  .card--brand .brand-lockup__dot { width: 120px; height: 120px; }
  .card--brand .brand-lockup__name { font-size: 26px; }

  .divider {
    position: absolute;
    left: 300px;
    top: 70px;
    width: 1px;
    height: 260px;
    background: var(--divider);
  }

  .contact {
    position: absolute;
    left: 330px;
    top: 80px;
    right: 24px;
    color: var(--text);
    font-size: 14px;
    line-height: 1.45;
  }
  .contact__name {
    font-family: "Michroma", sans-serif;
    color: var(--accent);
    font-size: 19px;
    letter-spacing: .08em;
    text-transform: uppercase;
  }
  .contact__role { font-size: 15px; margin-bottom: 16px; }
  .contact__list { list-style: none; margin-bottom: 20px; }
  .contact__list li { display: flex; align-items: center; gap: 8px; }
  .contact__list svg { width: 14px; height: 14px; flex: none; }
  .accent { color: var(--accent); }
  .contact__address { font-style: normal; font-size: 15px; }
</style>
</head>
<body>

  <section class="card card--contact" aria-label="Kontaktseite">
    <div class="brand-lockup">
      <span class="brand-lockup__dot"></span>
      <span class="brand-lockup__name">Marta Keller<br>Sport &amp; Events</span>
    </div>

    <div class="divider"></div>

    <div class="contact">
      <h1 class="contact__name">Marta Keller</h1>
      <p class="contact__role">Owner</p>
      <ul class="contact__list">
        <li>
          <svg viewBox="0 0 16 16" aria-hidden="true"><path d="M3 1.5l3 3-1.6 1.8a9 9 0 0 0 5.3 5.3L11.5 10l3 3-2 2C7 15 1 9 1 3.5z" fill="var(--accent)"/></svg>
          +49 69 / 31 52 94 07
        </li>
        <li>
          <svg viewBox="0 0 16 16" aria-hidden="true"><rect x="1" y="3" width="14" height="10" fill="var(--accent)"/><path d="M1 3l7 6 7-6" fill="none" stroke="#0b0b0b" stroke-width="1.4"/></svg>
          info@marta-keller-sport.example
        </li>
        <li>
          <svg viewBox="0 0 16 16" aria-hidden="true"><g fill="none" stroke="var(--accent)" stroke-width="1.4"><circle cx="8" cy="8" r="6.5"/><ellipse cx="8" cy="8" rx="3" ry="6.5"/><path d="M1.5 8h13M2.5 4.5h11M2.5 11.5h11"/></g></svg>
          <span>www.<span class="accent">marta-keller-sport</span>.example</span>
        </li>
      </ul>
      <address class="contact__address">
        <span class="accent">Marta Keller Sports &amp; Events</span><br>
        Birkendorfer Weg 14<br>
        D-63158 Offenbach
      </address>
    </div>
  </section>

  <section class="card card--brand" aria-label="Logoseite">
    <div class="brand-lockup">
      <span class="brand-lockup__dot"></span>
      <span class="brand-lockup__name">Marta Keller<br>Sport &amp; Events</span>
    </div>
  </section>

</body>
</html>
```